I am wanting to develop a new range of products called “BRISK LINE”. It will be 500mL trigger bottles of ready to use cleaning products. A Window&Glass Cleaner, Surface Sanitiser, Room Deodourant, Stainless Steel Rub, Spray&Wipe and a Sanitising Spray & Wipe. The label dimensions and shape are attached. Pellham is the shape I want but I do not like the design so don't base your design on it. SCOURBLAZE is a design I like I also like the design on the coffee packaging.

Target Market(s)

Retail and commercial kitchen

Industry/Entity Type

Cleaning Product

```html
<!DOCTYPE html>
<html lang="en">
<head>
<meta charset="utf-8">
<title>BRISK LINE – Ready to Use Trigger Spray Labels</title>
<link href="https://fonts.googleapis.com/css2?family=Russo+One&family=Varela+Round&display=swap" rel="stylesheet">
<style>
  :root {
    --bg: #ffffff;
    --ink: #111111;
    --flash: #f5ea00;
    --flash-edge: #1c1600;
    --glass: #1aa5e0;
    --surface: #e8345f;
    --room: #f29a2e;
    --steel: #7b3f98;
    --wipe: #2ea55a;
    --sanitise: #e52d8e;
  }
  * { box-sizing: border-box; margin: 0; padding: 0; }
  html, body {
    width: 1200px; height: 511px; overflow: hidden;
    background: var(--bg);
  }
  .range {
    width: 1200px; height: 511px;
    display: flex; justify-content: center; align-items: center;
    gap: 40px;
  }
  .label {
    --tone: var(--glass);
    --outline: -1px -1px 0 var(--flash-edge), 1px -1px 0 var(--flash-edge),
               -1px 1px 0 var(--flash-edge), 1px 1px 0 var(--flash-edge),
               0 1px 0 var(--flash-edge), 0 -1px 0 var(--flash-edge),
               1px 0 0 var(--flash-edge), -1px 0 0 var(--flash-edge);
    position: relative;
    width: 160px; height: 200px;
    clip-path: polygon(0 13%, 100% 0, 100% 100%, 0 100%);
    font-family: "Varela Round", sans-serif;
    color: var(--ink);
  }
  .label--glass { --tone: var(--glass); }
  .label--surface { --tone: var(--surface); }
  .label--room { --tone: var(--room); }
  .label--steel { --tone: var(--steel); }
  .label--wipe { --tone: var(--wipe); }
  .label--sanitise { --tone: var(--sanitise); }

  .label-art {
    position: absolute; inset: 0;
    background:
      radial-gradient(ellipse 70% 20% at 55% 44%, rgba(255,255,255,0.95) 0%, rgba(255,255,255,0.75) 55%, rgba(255,255,255,0) 100%),
      radial-gradient(circle at 20% 25%, rgba(255,255,255,0.35), rgba(255,255,255,0) 45%),
      var(--tone);
  }
  .label-flash {
    position: absolute; top: 0; right: 0;
    width: 78px; height: 78px;
    background: var(--flash);
    clip-path: polygon(18% 0, 100% 0, 100% 82%);
  }
  .label-flash span {
    position: absolute; top: 14px; right: -2px;
    transform: rotate(32deg);
    font-family: "Russo One", sans-serif;
    font-size: 14px; color: var(--ink);
  }
  .label-tagline {
    position: absolute; top: 34px; left: 8px;
    transform: rotate(-9deg);
    transform-origin: left center;
    font-family: "Russo One", sans-serif;
    font-size: 10px; letter-spacing: 0.3px;
    color: var(--flash);
    text-shadow: var(--outline);
    white-space: nowrap;
  }
  .label-brand {
    position: absolute; top: 76px; left: 0; right: 0;
    display: flex; align-items: center; justify-content: center; gap: 6px;
    font-size: 22px; line-height: 1; color: var(--ink);
    white-space: nowrap;
  }
  .label-brand i {
    width: 10px; height: 10px; border-radius: 50%;
    background: var(--tone); display: block;
  }
  .label-product {
    position: absolute; top: 124px; left: 10px; right: 6px;
    transform: rotate(-9deg);
    font-size: 15px; line-height: 1.1;
    color: var(--flash);
    text-shadow: var(--outline);
    white-space: nowrap;
  }
  .label-product .line2 { display: block; padding-left: 26px; }
  .label-volume {
    position: absolute; bottom: 10px; right: 14px;
    transform: rotate(-9deg);
    font-family: "Russo One", sans-serif;
    font-size: 12px; color: var(--flash);
    text-shadow: var(--outline);
  }
</style>
</head>
<body>
<main class="range">
  <article class="label label--glass">
    <div class="label-art" role="img" aria-label="Blue swirling wave pattern with white light streaks"></div>
    <div class="label-flash"><span>NEW!</span></div>
    <p class="label-tagline">READY TO USE</p>
    <h2 class="label-brand">BRISK LINE <i></i></h2>
    <p class="label-product">Window &amp;<span class="line2">Glass Cleaner</span></p>
    <p class="label-volume">500ml</p>
  </article>
  <article class="label label--surface">
    <div class="label-art" role="img" aria-label="Red swirling wave pattern with white light streaks"></div>
    <div class="label-flash"><span>NEW!</span></div>
    <p class="label-tagline">READY TO USE</p>
    <h2 class="label-brand">BRISK LINE <i></i></h2>
    <p class="label-product">Surface<span class="line2">Sanitiser</span></p>
    <p class="label-volume">500ml</p>
  </article>
  <article class="label label--room">
    <div class="label-art" role="img" aria-label="Orange swirling wave pattern with white light streaks"></div>
    <div class="label-flash"><span>NEW!</span></div>
    <p class="label-tagline">READY TO USE</p>
    <h2 class="label-brand">BRISK LINE <i></i></h2>
    <p class="label-product">Room<span class="line2">Deodourant</span></p>
    <p class="label-volume">500ml</p>
  </article>
  <article class="label label--steel">
    <div class="label-art" role="img" aria-label="Purple swirling wave pattern with white light streaks"></div>
    <div class="label-flash"><span>NEW!</span></div>
    <p class="label-tagline">READY TO USE</p>
    <h2 class="label-brand">BRISK LINE <i></i></h2>
    <p class="label-product">Stainless<span class="line2">Steel Rub</span></p>
    <p class="label-volume">500ml</p>
  </article>
  <article class="label label--wipe">
    <div class="label-art" role="img" aria-label="Green swirling wave pattern with white light streaks"></div>
    <div class="label-flash"><span>NEW!</span></div>
    <p class="label-tagline">READY TO USE</p>
    <h2 class="label-brand">BRISK LINE <i></i></h2>
    <p class="label-product">Spray &amp;<span class="line2">Wipe</span></p>
    <p class="label-volume">500ml</p>
  </article>
  <article class="label label--sanitise">
    <div class="label-art" role="img" aria-label="Pink swirling wave pattern with white light streaks"></div>
    <div class="label-flash"><span>NEW!</span></div>
    <p class="label-tagline">READY TO USE</p>
    <h2 class="label-brand">BRISK LINE <i></i></h2>
    <p class="label-product">Sanitising<span class="line2">Spray &amp; Wipe.</span></p>
    <p class="label-volume">500ml</p>
  </article>
</main>
</body>
</html>
```